Business Cards for Brightpath MD a Medical Billing company
Brightpath MD
Business Cards for Brightpath MD a  Medical Billing company - Medical
Creative Brief
Modern
Renata Morvel
President
I don't want to use my address on the cards
513-555-0148 ext 2047
renatamorvel@brightpathmd.example
www.brightpathmd.example
list social media Twitter @BrightpathMD Facebook Brightpath MD Hopefully my new website will be launched this week
I am looking for ideas last time I listed what services we offer but not sure I should do this again

```html
<!DOCTYPE html>
<html lang="en">
<head>
<meta charset="utf-8">
<title>Brightpath MD — Business Card</title>
<link rel="stylesheet" href="https://fonts.googleapis.com/css2?family=Crimson+Text:wght@400;600&family=Open+Sans:wght@400&display=swap">
<style>
  :root {
    --backdrop: #e6e3e0;
    --card-dark: #0d0d0e;
    --card-dark-edge: #2a2a2c;
    --card-light: #f1f2f3;
    --card-light-edge: #d9dcde;
    --brand-green: #8db32c;
    --brand-blue: #1f6fb8;
    --ink: #1c1c1c;
    --icon: #3b7fc0;
  }
  html, body {
    margin: 0;
    width: 1200px;
    height: 969px;
    overflow: hidden;
    background: var(--backdrop);
  }
  .business-card {
    position: absolute;
    left: 100px;
    top: 202px;
    width: 1000px;
    height: 566px;
    border-radius: 30px;
    overflow: hidden;
    box-shadow: 0 18px 40px rgba(0,0,0,0.18);
  }
  .business-card svg { display: block; }
  .serif { font-family: "Crimson Text", Georgia, serif; }
  .sans { font-family: "Open Sans", Arial, sans-serif; }
  .brand-name { font-size: 60px; font-weight: 600; fill: var(--brand-blue); }
  .holder-name { font-size: 38px; font-weight: 600; letter-spacing: 1.5px; fill: var(--brand-blue); }
  .holder-title { font-size: 24px; fill: var(--brand-green); }
  .contact-line { font-size: 24px; fill: var(--ink); }
  .social-line { font-size: 22px; fill: var(--ink); }
</style>
</head>
<body>
<div class="business-card">
  <svg width="1000" height="566" viewBox="0 0 1000 566" xmlns="http://www.w3.org/2000/svg">
    <defs>
      <linearGradient id="frost" x1="0" y1="0" x2="0" y2="1">
        <stop offset="0" stop-color="var(--card-light)"/>
        <stop offset="1" stop-color="var(--card-light-edge)"/>
      </linearGradient>
      <linearGradient id="night" x1="0" y1="0" x2="0" y2="1">
        <stop offset="0" stop-color="var(--card-dark-edge)"/>
        <stop offset="1" stop-color="var(--card-dark)"/>
      </linearGradient>
    </defs>

    <!-- light lower panel -->
    <rect class="panel-light" width="1000" height="566" fill="url(#frost)"/>

    <!-- accent wave stripes -->
    <path class="wave-blue" d="M0 328 C220 336 380 330 520 250 C650 176 780 128 1000 140 L1000 160 C790 150 660 196 530 268 C390 346 220 352 0 344 Z" fill="var(--brand-blue)"/>
    <path class="wave-green" d="M0 318 C220 326 380 320 520 240 C650 166 780 118 1000 130 L1000 144 C785 136 655 184 525 258 C385 336 220 340 0 334 Z" fill="var(--brand-green)"/>

    <!-- dark upper panel -->
    <path class="panel-dark" d="M0 0 H1000 V130 C780 118 650 166 520 240 C380 320 220 326 0 318 Z" fill="url(#night)"/>

    <!-- brand name -->
    <text class="serif brand-name" x="55" y="140">Brightpath MD</text>

    <!-- holder -->
    <text class="serif holder-name" x="928" y="314" text-anchor="end">RENATA MORVEL</text>
    <text class="serif holder-title" x="928" y="346" text-anchor="end">President</text>

    <!-- contact lines -->
    <text class="serif contact-line" x="878" y="410" text-anchor="end">513-555-0148 ext 2047</text>
    <text class="serif contact-line" x="878" y="446" text-anchor="end">513-555-0193</text>
    <text class="serif contact-line" x="878" y="484" text-anchor="end">renatamorvel@brightpathmd.example</text>
    <text class="serif contact-line" x="878" y="522" text-anchor="end">www.brightpathmd.example</text>

    <!-- contact icons -->
    <g class="icon-phone" fill="var(--icon)">
      <rect x="900" y="397" width="22" height="6" rx="3"/>
      <rect x="903" y="402" width="16" height="11" rx="2"/>
    </g>
    <g class="icon-mobile" fill="none" stroke="var(--icon)" stroke-width="2.5">
      <rect x="904" y="428" width="14" height="24" rx="3"/>
    </g>
    <g class="icon-mail" fill="none" stroke="var(--icon)" stroke-width="2.5">
      <rect x="900" y="470" width="22" height="15" rx="1"/>
      <path d="M900 470 L911 479 L922 470"/>
    </g>
    <g class="icon-web" fill="none" stroke="var(--icon)" stroke-width="2">
      <circle cx="911" cy="515" r="10"/>
      <ellipse cx="911" cy="515" rx="4.5" ry="10"/>
      <path d="M901 515 H921"/>
    </g>

    <!-- social -->
    <rect class="social-marker" x="58" y="428" width="20" height="20" rx="2" fill="var(--icon)"/>
    <text class="sans social-line" x="96" y="446">Brightpath MD</text>
    <rect class="social-marker" x="58" y="466" width="20" height="20" rx="2" fill="var(--icon)"/>
    <text class="sans social-line" x="96" y="484">@BrightpathMD</text>
  </svg>
</div>
</body>
</html>
```